Veltrano - Mechanic/Collision Center Business Card

We're looking for a business card design for our mechanic/ collision repair shop.

Can be with colours or monochromatic.

See the attached files.

Many thanks

```html
<!DOCTYPE html>
<html lang="en">
<head>
<meta charset="utf-8">
<title>Veltrano – Business Card</title>
<link rel="stylesheet" href="https://fonts.googleapis.com/css2?family=Roboto:wght@400;500;700&display=swap">
<style>
  :root {
    --brand-blue: #1e9ad6;
    --ink: #1b1d1f;
    --band: #16181a;
    --paper: #fbfbf9;
    --text-grey: #55585b;
    --divider: #b9bcbe;
    --stage: #e4e5e7;
  }
  * { box-sizing: border-box; margin: 0; padding: 0; }
  html, body {
    width: 1200px; height: 874px; overflow: hidden;
    background: var(--stage);
    font-family: "Roboto", Arial, sans-serif;
  }
  .sheet {
    width: 1200px; height: 874px;
    display: flex; flex-direction: column; align-items: center; justify-content: center;
    gap: 36px;
  }
  .card {
    width: 660px; height: 377px; position: relative; overflow: hidden;
    box-shadow: 0 6px 18px rgba(0,0,0,.18);
  }

  /* front */
  .card-front { background: var(--brand-blue); }
  .front-brand {
    position: absolute; left: 0; right: 0; top: 0; height: 280px;
    display: flex; align-items: center; justify-content: center; gap: 18px;
  }
  .brand-mark { width: 34px; height: 34px; background: var(--ink); border-radius: 50%; }
  .front-name {
    font-weight: 700; font-size: 86px; letter-spacing: 2px;
    color: var(--ink); text-transform: uppercase;
  }
  .front-band {
    position: absolute; left: 0; right: 0; bottom: 0; height: 97px;
    background: var(--band);
    display: flex; align-items: center; justify-content: center;
  }
  .website {
    color: #f2f2f2; font-size: 19px; letter-spacing: 4px; font-weight: 500;
  }

  /* back */
  .card-back { background: var(--paper); }
  .back-brand {
    position: absolute; left: 0; right: 0; top: 52px;
    display: flex; align-items: center; justify-content: center; gap: 12px;
  }
  .back-brand .brand-mark { width: 22px; height: 22px; background: var(--brand-blue); border-radius: 0; }
  .back-name {
    font-weight: 700; font-size: 50px; letter-spacing: 1px;
    color: var(--ink); text-transform: uppercase;
  }
  .contact {
    position: absolute; left: 0; right: 0; top: 190px;
    display: flex; justify-content: center;
  }
  .person {
    text-align: right; padding-right: 26px; border-right: 1px solid var(--divider);
    color: var(--text-grey); font-size: 17px; line-height: 1.3;
  }
  .person-name { color: var(--brand-blue); font-size: 24px; font-weight: 500; letter-spacing: .5px; }
  .person-title { color: var(--ink); font-size: 18px; margin-bottom: 2px; }
  .lines { list-style: none; padding-left: 22px; padding-top: 30px; color: var(--text-grey); font-size: 17px; line-height: 1.45; }
  .lines li { display: flex; align-items: center; gap: 10px; }
  .lines svg { width: 15px; height: 15px; fill: var(--brand-blue); flex: none; }
</style>
</head>
<body>
<main class="sheet">
  <section class="card card-front">
    <div class="front-brand">
      <span class="brand-mark"></span>
      <span class="front-name">Veltrano</span>
    </div>
    <div class="front-band">
      <span class="website">WWW.VELTRANO.COM</span>
    </div>
  </section>

  <section class="card card-back">
    <div class="back-brand">
      <span class="brand-mark"></span>
      <span class="back-name">Veltrano</span>
    </div>
    <div class="contact">
      <div class="person">
        <p class="person-name">DANIEL ROURKE</p>
        <p class="person-title">President</p>
        <p>4120 Harbor View Road</p>
        <p>Juneau, Alaska 99801</p>
      </div>
      <ul class="lines">
        <li><svg viewBox="0 0 16 16"><path d="M3.5 1l2.5 3-1.5 2c1 2 3 4 5 5l2-1.5 3 2.5-1.5 2.5C8 15 1 8 1 2.5z"/></svg>555-214-7730</li>
        <li><svg viewBox="0 0 16 16"><path d="M4 0h8a1 1 0 0 1 1 1v14a1 1 0 0 1-1 1H4a1 1 0 0 1-1-1V1a1 1 0 0 1 1-1zm1 2v10h6V2zm3 11a1 1 0 1 0 0 2 1 1 0 0 0 0-2z"/></svg>555-618-2049</li>
        <li><svg viewBox="0 0 16 16"><path d="M4 1h8v4H4zM1 6h14v7h-3v2H4v-2H1zm4 5v3h6v-3z"/></svg>555-307-4462</li>
        <li><svg viewBox="0 0 16 16"><path d="M1 3h14v10H1zm1 1.2V5l6 4 6-4v-.8z"/></svg>info@veltrano.com</li>
      </ul>
    </div>
  </section>
</main>
</body>
</html>
```